Website for keystone mobile detailing.

Need a homepage, pages for: car and truck detailing, boat detailing, airplane detailing, about us, contact us. I have the domain name through nimbuspark so I will need the design uploaded on my domain. Also hoping to link other domains to this page.I would like to see the logo more pronounced. I would like to see a large phone number link to call my business. The layout looks nice but the pics need to depict car washing and waxing not car mechanics. i would like the colors of the webpage to incorporate the colors found in the logo in some way. I would like links to social media pages

Target Market(s)

Local customers in Vero Beach, Florida.

Number of Pages Required

5+ page

Colors

Designer to choose colors to be used in the design.

Requirements
Must have
• Easy to navigate, attractive pages with pictures and logo, professional looking. must have my phone number and logo very prevalent and links to call or go to home page. I would like links to my social media accounts on the home page.
Nice to have
• Easy to navigate, attractive pages with pictures and logo, professional looking.

```html
<!DOCTYPE html>
<html lang="en">
<head>
<meta charset="utf-8">
<title>Keystone Mobile Detailing</title>
<link rel="stylesheet" href="https://fonts.googleapis.com/css2?family=Poppins:wght@400;500;600;700;800&display=swap">
<style>
:root{
  --blue:#1616d8;
  --sky:#3ec4f2;
  --red:#e3141f;
  --dark:#17191d;
  --darker:#101216;
  --white:#ffffff;
  --ink:#1d1d1d;
}
*{margin:0;padding:0;box-sizing:border-box}
html,body{width:1200px;height:4147px;overflow:hidden}
body{font-family:'Poppins',sans-serif;background:var(--white);color:var(--ink);position:relative}
section,header,footer{position:absolute;left:0;width:1200px}
.abs{position:absolute}
.center{left:0;width:1200px;text-align:center}

/* header */
.site-header{top:0;height:144px;background:var(--white)}
.header-bg{position:absolute;inset:0}
.brand{left:60px;top:32px;font-weight:700;font-size:30px;line-height:36px;color:var(--blue);width:330px}
.top-phone{left:585px;top:6px;height:56px;display:flex;align-items:center;gap:14px;color:var(--white);font-weight:600;font-size:44px}
.social-mini{left:960px;top:14px;display:flex;gap:10px}
.social-mini span{width:40px;height:40px;border-radius:50%;background:var(--white);opacity:.95}
.nav{left:516px;top:88px;display:flex;gap:0}
.nav a{color:var(--white);text-decoration:none;font-weight:600;font-size:23px;padding:0 33px;line-height:40px}

/* hero */
.hero{top:144px;height:644px;background:linear-gradient(180deg,#2b2d30 0%,#1a1c1f 55%,#121315 100%)}
.hero-title{top:130px;font-weight:700;font-size:62px;line-height:72px;color:var(--white)}
.select{top:308px;width:354px;height:62px;border:3px solid var(--white);color:var(--white);font-weight:600;font-size:22px;display:flex;align-items:center;padding:0 24px;gap:14px}
.select .caret{margin-left:auto;font-size:18px}
.btn{top:396px;width:354px;height:60px;display:flex;align-items:center;justify-content:center;font-weight:600;font-size:22px;color:var(--white);text-transform:uppercase}
.btn-sky{left:236px;background:var(--sky)}
.btn-red{left:612px;background:var(--red)}
.call-label{top:460px;font-weight:700;font-size:34px;color:var(--white)}
.call-number{top:500px;font-weight:700;font-size:96px;line-height:110px;color:var(--sky);letter-spacing:2px}

/* about */
.about{top:788px;height:594px;background:var(--white)}
.section-title{font-weight:800;font-size:46px;text-transform:uppercase}
.about-title{top:40px;color:var(--blue)}
.about-text{top:103px;left:200px;width:800px;text-align:center;font-size:22px;line-height:32px;color:var(--ink)}
.hex-card{top:192px;width:250px;text-align:center}
.hex-card svg{display:block;margin:0 auto}
.hex-card h3{margin-top:30px;font-weight:600;font-size:28px;color:var(--sky)}
.hex-card p{font-size:17px;line-height:22px;color:#333;width:200px;margin:0 auto}

/* services */
.services{top:1382px;height:830px;background:linear-gradient(180deg,#22252a,#15171a)}
.services-title{top:60px;color:var(--white)}
.services-text{top:126px;left:90px;width:1020px;text-align:center;font-size:21px;line-height:28px;color:#d8d8d8}
.service{width:300px;text-align:center}
.service svg{display:block;margin:0 auto}
.service h4{margin-top:16px;font-weight:600;font-size:20px;color:var(--white)}

/* gallery */
.gallery{top:2212px;height:769px;background:var(--white)}
.gallery-title{top:40px;color:var(--red)}
.photo{width:282px;height:222px;background:linear-gradient(135deg,#3d4852,#6b7580 45%,#2a3038)}
.photo.active{background:linear-gradient(135deg,#c21c43,#d63a5d 50%,#a5142f)}

/* map */
.map{top:2981px;height:531px;background:linear-gradient(135deg,#e9e6df,#dedad2 60%,#cfd9de)}

/* footer */
.site-footer{top:3512px;height:635px;background:linear-gradient(180deg,#1f2226,#121417)}
.footer-col h5{font-weight:700;font-size:34px;color:var(--white);text-transform:uppercase;margin-bottom:44px}
.footer-col li{list-style:none;font-size:24px;color:var(--white);height:70px;display:flex;align-items:flex-start;gap:22px}
.tri{width:0;height:0;border-left:15px solid var(--white);border-top:11px solid transparent;border-bottom:11px solid transparent;margin-top:5px}
.dot{width:40px;height:40px;border-radius:50%;flex:none;margin-top:-4px}
.copyright{top:548px;font-size:20px;font-weight:600;color:var(--white)}
.copyright em{font-style:normal;color:var(--sky)}
</style>
</head>
<body>

<header class="site-header">
  <svg class="header-bg" width="1200" height="144" viewBox="0 0 1200 144" aria-hidden="true">
    <polygon points="520,0 1200,0 1200,70 460,70" fill="var(--sky)"/>
    <polygon points="470,62 1200,62 1200,144 340,144" fill="var(--blue)"/>
  </svg>
  <div class="abs brand">Keystone Mobile Detailing</div>
  <div class="abs top-phone">
    <svg width="40" height="40" viewBox="0 0 24 24" aria-hidden="true"><path fill="#fff" d="M6.6 10.8a15 15 0 0 0 6.6 6.6l2.2-2.2a1 1 0 0 1 1-.25 11.4 11.4 0 0 0 3.6.57 1 1 0 0 1 1 1V20a1 1 0 0 1-1 1A17 17 0 0 1 3 4a1 1 0 0 1 1-1h3.5a1 1 0 0 1 1 1c0 1.25.2 2.45.57 3.57a1 1 0 0 1-.25 1z"/></svg>
    555-218-4730
  </div>
  <div class="abs social-mini"><span></span><span></span><span></span><span></span></div>
  <nav class="abs nav">
    <a href="#">HOME</a><a href="#">ABOUT US</a><a href="#">SERVICES&#8744;</a><a href="#">CONTACT</a>
  </nav>
</header>

<section class="hero" role="img" aria-label="Background photo of a car being hand washed and waxed">
  <h1 class="abs center hero-title">GET YOUR CAR REPAIR<br>SERVICES NOW!</h1>
  <div class="abs select" style="left:236px">
    <svg width="30" height="24" viewBox="0 0 30 24" aria-hidden="true"><path fill="#fff" d="M5 9l3-7h14l3 7h2v9h-3v4h-4v-4H10v4H6v-4H3V9z"/><circle cx="8" cy="14" r="2" fill="#222"/><circle cx="22" cy="14" r="2" fill="#222"/></svg>
    Select Vehicle <span class="caret">&#8744;</span>
  </div>
  <div class="abs select" style="left:612px">
    <svg width="22" height="28" viewBox="0 0 22 28" aria-hidden="true"><path fill="#fff" d="M11 0a10 10 0 0 1 10 10c0 8-10 18-10 18S1 18 1 10A10 10 0 0 1 11 0z"/><circle cx="11" cy="10" r="4" fill="#222"/></svg>
    Select Location <span class="caret">&#8744;</span>
  </div>
  <a class="abs btn btn-sky">Get an appointment</a>
  <a class="abs btn btn-red">Contact us</a>
  <p class="abs center call-label">OR CALL US NOW!</p>
  <p class="abs center call-number">555-218-4730</p>
</section>

<section class="about">
  <h2 class="abs center section-title about-title">Who we are?</h2>
  <p class="abs about-text">Spare tip hamburger cow ribs ham jowl chicken andouille ham flank pig pig belly brisket cow loin ham tenderloin. Leberkas steak ball brisket strip.</p>

  <div class="abs hex-card" style="left:55px">
    <svg width="208" height="224" viewBox="0 0 208 224" aria-hidden="true"><polygon points="104,6 198,58 198,166 104,218 10,166 10,58" fill="none" stroke="var(--blue)" stroke-width="12"/><path fill="var(--red)" d="M50 120l40-6 26-40c4-6 14-4 12 4l-10 34 38-4 10-12h8l-4 22 4 22h-8l-10-12-38-4 10 34c2 8-8 10-12 4l-26-40-40-6z"/></svg>
    <h3>We Care For You</h3><p>lorem ipsum door alis amet, lorem dolor dolor</p>
  </div>
  <div class="abs hex-card" style="left:334px">
    <svg width="208" height="224" viewBox="0 0 208 224" aria-hidden="true"><polygon points="104,6 198,58 198,166 104,218 10,166 10,58" fill="none" stroke="var(--blue)" stroke-width="12"/><rect x="42" y="78" width="80" height="56" fill="var(--red)"/><path fill="var(--red)" d="M126 94h24l16 20v20h-40z"/><circle cx="64" cy="140" r="10" fill="var(--red)"/><circle cx="146" cy="140" r="10" fill="var(--red)"/></svg>
    <h3>We Care For You</h3><p>lorem ipsum door alis amet, lorem dolor dolor</p>
  </div>
  <div class="abs hex-card" style="left:616px">
    <svg width="208" height="224" viewBox="0 0 208 224" aria-hidden="true"><polygon points="104,6 198,58 198,166 104,218 10,166 10,58" fill="none" stroke="var(--blue)" stroke-width="12"/><rect x="98" y="62" width="10" height="22" fill="var(--red)"/><rect x="72" y="84" width="64" height="22" fill="var(--red)"/><path fill="var(--red)" d="M40 110h128l-16 34H56z"/><path d="M48 154q14-8 28 0t28 0 28 0 28 0" stroke="var(--red)" stroke-width="5" fill="none"/></svg>
    <h3>We Care For You</h3><p>lorem ipsum door alis amet, lorem dolor dolor</p>
  </div>
  <div class="abs hex-card" style="left:898px">
    <svg width="208" height="224" viewBox="0 0 208 224" aria-hidden="true"><polygon points="104,6 198,58 198,166 104,218 10,166 10,58" fill="none" stroke="var(--blue)" stroke-width="12"/><path fill="var(--red)" d="M44 112l12-28h96l12 28h6v26H38v-26z"/><path fill="#fff" d="M62 108l8-18h28v18zM106 108V90h28l8 18z"/><circle cx="72" cy="138" r="11" fill="var(--red)"/><circle cx="136" cy="138" r="11" fill="var(--red)"/></svg>
    <h3>We Care For You</h3><p>lorem ipsum door alis amet, lorem dolor dolor</p>
  </div>
</section>

<section class="services" role="img" aria-label="Dark background photo of a detailer working on a vehicle">
  <h2 class="abs center section-title services-title">What we do?</h2>
  <p class="abs services-text">Lorem ipsum dolor sit amet, consectetur adipisicing elit, sed do eiusmod tempor incididunt ut labore et dolore magna aliqua. Ut enim ad minim veniam, quis nostrud exercitation ullamco laboris nisi ut aliquip ex ea commodo consequat. Duis aute irure dolor in reprehenderit in velit esse cillum dolore eu fugiat nulla pariatur. Excepteur sint occaecat cupidatat non proident.</p>

  <div class="abs service" style="left:77px;top:300px">
    <svg width="140" height="140" viewBox="0 0 140 140" aria-hidden="true"><circle cx="64" cy="74" r="54" fill="var(--sky)"/><circle cx="64" cy="74" r="16" fill="#1c1e22"/><path d="M90 16a64 64 0 0 1 38 46" stroke="var(--sky)" stroke-width="12" fill="none"/></svg>
    <h4>Break Checkup</h4>
  </div>
  <div class="abs service" style="left:447px;top:300px">
    <svg width="140" height="140" viewBox="0 0 140 140" aria-hidden="true"><rect x="14" y="14" width="8" height="112" fill="var(--sky)"/><rect x="118" y="14" width="8" height="112" fill="var(--sky)"/><rect x="14" y="14" width="112" height="8" fill="var(--sky)"/><path fill="var(--sky)" d="M34 96l8-22h56l8 22v20H34z"/><rect x="40" y="36" width="6" height="18" fill="var(--sky)"/><rect x="66" y="36" width="6" height="18" fill="var(--sky)"/><rect x="92" y="36" width="6" height="18" fill="var(--sky)"/></svg>
    <h4>Odor Elimination</h4>
  </div>
  <div class="abs service" style="left:829px;top:300px">
    <svg width="140" height="140" viewBox="0 0 140 140" aria-hidden="true"><rect x="40" y="10" width="30" height="14" fill="var(--sky)"/><rect x="32" y="26" width="46" height="96" rx="10" fill="none" stroke="var(--sky)" stroke-width="10"/><path fill="var(--sky)" d="M82 56l44-24v80L82 88z"/></svg>
    <h4>Engine Repair</h4>
  </div>
  <div class="abs service" style="left:77px;top:536px">
    <svg width="140" height="140" viewBox="0 0 140 140" aria-hidden="true"><path fill="none" stroke="var(--sky)" stroke-width="8" d="M24 60h70l30-14v6L98 96H36z"/><rect x="52" y="46" width="24" height="14" fill="var(--sky)"/><circle cx="122" cy="78" r="6" fill="var(--sky)"/></svg>
    <h4>Oil Change</h4>
  </div>
  <div class="abs service" style="left:447px;top:536px">
    <svg width="140" height="140" viewBox="0 0 140 140" aria-hidden="true"><circle cx="70" cy="70" r="46" fill="none" stroke="var(--sky)" stroke-width="10" stroke-dasharray="18 10"/><circle cx="70" cy="70" r="26" fill="none" stroke="var(--sky)" stroke-width="8"/><path d="M52 88l36-36" stroke="var(--sky)" stroke-width="8"/></svg>
    <h4>Inspection Service</h4>
  </div>
  <div class="abs service" style="left:829px;top:536px">
    <svg width="140" height="140" viewBox="0 0 140 140" aria-hidden="true"><circle cx="70" cy="70" r="58" fill="var(--sky)"/><circle cx="70" cy="70" r="40" fill="#1c1e22"/><circle cx="70" cy="70" r="10" fill="var(--sky)"/><path d="M70 32v76M32 70h76M43 43l54 54M97 43l-54 54" stroke="var(--sky)" stroke-width="6"/></svg>
    <h4>Wheel Service</h4>
  </div>
</section>

<section class="gallery">
  <h2 class="abs center section-title gallery-title">Gallery</h2>
  <div class="abs photo" style="left:91px;top:138px" role="img" aria-label="Photo of a gloved hand cleaning a car"></div>
  <div class="abs photo" style="left:459px;top:138px" role="img" aria-label="Photo of a gloved hand cleaning a car"></div>
  <div class="abs photo" style="left:835px;top:138px" role="img" aria-label="Photo of a gloved hand cleaning a car"></div>
  <div class="abs photo" style="left:91px;top:470px" role="img" aria-label="Photo of a gloved hand cleaning a car"></div>
  <div class="abs photo active" style="left:459px;top:470px" role="img" aria-label="Highlighted gallery photo of car detailing">
    <svg class="abs" style="left:111px;top:81px" width="60" height="60" viewBox="0 0 60 60" aria-hidden="true"><circle cx="30" cy="30" r="28" fill="#fff"/><ellipse cx="30" cy="30" rx="16" ry="10" fill="var(--red)"/><circle cx="30" cy="30" r="5" fill="#fff"/></svg>
  </div>
  <div class="abs photo" style="left:835px;top:470px" role="img" aria-label="Photo of a gloved hand cleaning a car"></div>
</section>

<section class="map" role="img" aria-label="Street map of the business location in Vero Beach"></section>

<footer class="site-footer">
  <div class="abs footer-col" style="left:119px;top:80px">
    <h5>Our Services</h5>
    <ul>
      <li><span class="tri"></span>Car Detailing</li>
      <li><span class="tri"></span>Truck Detailing</li>
      <li><span class="tri"></span>Boat Detailing</li>
      <li><span class="tri"></span>Airplane Detailing</li>
    </ul>
  </div>
  <div class="abs footer-col" style="left:462px;top:80px">
    <h5>Contact Us</h5>
    <ul>
      <li>555-218-4730</li>
      <li>hello@keystonedetail.com</li>
      <li>88 Harbor Lane, Vero Beach</li>
    </ul>
  </div>
  <div class="abs footer-col" style="left:843px;top:80px">
    <h5>Like Us On</h5>
    <ul>
      <li><span class="dot" style="background:#2f64d8"></span>pagebook.com</li>
      <li><span class="dot" style="background:var(--sky)"></span>chirpline.com</li>
      <li><span class="dot" style="background:var(--red)"></span>pinboardly.com</li>
      <li><span class="dot" style="background:#7a4a3a"></span>snapgrid.com</li>
    </ul>
  </div>
  <p class="abs center copyright">© Copyrights 2018 <em>Company</em> | All Rights Reserved.</p>
</footer>

</body>
</html>
```